Cognitive therapist.

I am a therapist and my main work is with clients who have depression and anxiety disorders.

I need something reasonably plain. Cognitive therapy is a very pragmatic approach to dealing with problems, so it isn't new agey (no offence to new age therapies at all)

Hi everyone, I am currently looking at a particular design that I will most likely go with. Cheers, Lyn

Lyn Marchet
Cognitive Therapist
BA, PG Dip Mental Health,
PG Dip Cog Beh Therapy
MKRPG

The Quillan Rooms,
Level One
47 Harwick Parade
Cnr Drayfield St & Harwick Parade
P O Box 38 215
WELLINGTON 6287

Phone: 027 463 2851 Email: lmarchet@quorvane.co.nz

www.lynmarchet.co.nz

• No illustration, or colour. not old style fonts.

```html
<!DOCTYPE html>
<html lang="en">
<head>
<meta charset="utf-8">
<title>Lyn Marchet – Business Card</title>
<link rel="stylesheet" href="https://fonts.googleapis.com/css2?family=Questrial&family=Didact+Gothic&display=swap">
<style>
  :root {
    --backdrop: #d8d8d6;
    --card: #ffffff;
    --teal: #7ccdd3;
    --ink: #555555;
    --ink-strong: #444444;
    --rule: #8a8a8a;
  }
  * { box-sizing: border-box; margin: 0; padding: 0; }
  html, body {
    width: 1200px;
    height: 1200px;
    overflow: hidden;
    background: var(--backdrop);
  }
  .canvas {
    position: relative;
    width: 1200px;
    height: 1200px;
  }
  .card {
    position: absolute;
    left: 60px;
    top: 288px;
    width: 1080px;
    height: 624px;
    background: var(--card);
    border-radius: 54px;
    overflow: hidden;
    font-family: "Didact Gothic", "Questrial", sans-serif;
    color: var(--ink);
  }
  .identity {
    position: absolute;
    right: 563px;
    top: 244px;
    text-align: right;
  }
  .identity__name {
    font-family: "Questrial", sans-serif;
    font-size: 60px;
    line-height: 1;
    letter-spacing: 1px;
    color: var(--teal);
    font-weight: 400;
    text-transform: uppercase;
  }
  .identity__credentials {
    margin-top: 4px;
    margin-right: -15px;
    font-size: 22px;
    line-height: 31px;
  }
  .divider {
    position: absolute;
    left: 541px;
    top: 232px;
    width: 2px;
    height: 195px;
    background: var(--rule);
  }
  .contact {
    position: absolute;
    left: 579px;
    top: 227px;
    font-size: 23px;
    line-height: 31px;
    color: var(--ink);
  }
  .contact__postal strong {
    font-weight: 700;
    color: var(--ink-strong);
    font-family: "Questrial", sans-serif;
    -webkit-text-stroke: 0.6px var(--ink-strong);
  }
  .contact__direct {
    margin-top: 10px;
    list-style: none;
  }
  .contact__direct li {
    display: flex;
    align-items: center;
    gap: 4px;
    height: 31px;
  }
  .contact__icon {
    width: 24px;
    height: 24px;
    flex: none;
  }
  .web-strip {
    position: absolute;
    left: 0;
    right: 0;
    top: 560px;
    height: 40px;
  }
  .web-strip__band {
    position: absolute;
    top: 14px;
    height: 13px;
    background: var(--teal);
  }
  .web-strip__band--left { left: 0; width: 358px; }
  .web-strip__band--right { left: 722px; right: 0; }
  .web-strip__url {
    position: absolute;
    left: 0;
    right: 0;
    top: 0;
    text-align: center;
    font-size: 28px;
    line-height: 40px;
    color: var(--ink);
    letter-spacing: 0.5px;
  }
</style>
</head>
<body>
<main class="canvas">
  <section class="card" aria-label="Business card for Lyn Marchet">
    <div class="identity">
      <h1 class="identity__name">Lyn Marchet</h1>
      <p class="identity__credentials">
        Cognitive Therapist BA,<br>
        PG Dip Mental Health,<br>
        PG Dip Cog Beh Therapy MKRPG
      </p>
    </div>

    <div class="divider" aria-hidden="true"></div>

    <address class="contact" style="font-style:normal">
      <p class="contact__postal">
        The Quillan Rooms, Level One<br>
        47 Harwick Parade Cnr Drayfield St<br>
        &amp; Harwick Parade<br>
        <strong>P O Box</strong> 38 215 WELLINGTON 6287
      </p>
      <ul class="contact__direct">
        <li>
          <svg class="contact__icon" viewBox="0 0 24 24" aria-hidden="true">
            <circle cx="12" cy="12" r="11" fill="#7ccdd3"/>
            <rect x="8" y="5" width="8" height="14" rx="1.5" fill="none" stroke="#ffffff" stroke-width="1.6"/>
            <line x1="10.5" y1="16.5" x2="13.5" y2="16.5" stroke="#ffffff" stroke-width="1.4"/>
          </svg>
          <span>027 463 2851</span>
        </li>
        <li>
          <svg class="contact__icon" viewBox="0 0 24 24" aria-hidden="true">
            <circle cx="12" cy="12" r="11" fill="#7ccdd3"/>
            <rect x="6" y="8" width="12" height="8.5" rx="1" fill="none" stroke="#ffffff" stroke-width="1.6"/>
            <polyline points="6.5,8.5 12,13 17.5,8.5" fill="none" stroke="#ffffff" stroke-width="1.5"/>
          </svg>
          <span>lmarchet@quorvane.co.nz</span>
        </li>
      </ul>
    </address>

    <div class="web-strip">
      <div class="web-strip__band web-strip__band--left"></div>
      <div class="web-strip__band web-strip__band--right"></div>
      <p class="web-strip__url">www.lynmarchet.co.nz</p>
    </div>
  </section>
</main>
</body>
</html>
```